KTR Engineering Pty Ltd

I have already had Corvale welding and fabrication cards made , my business has changed too KTR engineering Pty Ltd so I need my logo changed on the cards
one side have my logo then the other side have what we do.
front side logo and details
owner /operator : Lachlan Meravic
email: ktr.works@ironvalemail.com
number: 0491537204
ABN: 47 261 538 902
ACN: 718 352 946
on back have in dot points what we do:
* structural steel erection
* precast panels
* site welding
*steel alteration & repair
* rigging & dogging
*labour hire
all details in breif

```html
<!DOCTYPE html>
<html lang="en">
<head>
<meta charset="utf-8">
<title>KTR Engineering Pty Ltd – Business Card</title>
<link href="https://fonts.googleapis.com/css2?family=Lato:wght@300;400;700;900&family=Montserrat:wght@700;800&display=swap" rel="stylesheet">
<style>
  :root {
    --navy: #16243a;
    --red: #9e3326;
    --tick: #b83a2b;
    --white: #ffffff;
    --grey: #6f737a;
    --stage: #2c2e33;
  }
  * { box-sizing: border-box; margin: 0; padding: 0; }
  html, body { width: 1200px; height: 952px; overflow: hidden; }
  body {
    background: var(--stage);
    display: flex;
    flex-direction: column;
    align-items: center;
    justify-content: center;
    gap: 56px;
    font-family: "Lato", sans-serif;
  }
  .card {
    position: relative;
    width: 700px;
    height: 400px;
    border-radius: 24px;
    overflow: hidden;
  }

  /* Front */
  .card-front { background: var(--white); }
  .company-name {
    position: absolute;
    top: 78px;
    left: 300px;
    font-family: "Montserrat", sans-serif;
    font-weight: 800;
    font-size: 30px;
    letter-spacing: 1px;
    color: var(--navy);
    text-transform: uppercase;
    line-height: 1.1;
  }
  .owner {
    position: absolute;
    top: 190px;
    left: 70px;
  }
  .owner-name {
    font-size: 24px;
    letter-spacing: 0.5px;
    text-transform: uppercase;
  }
  .owner-name .first { color: var(--red); font-weight: 400; }
  .owner-name .last { color: var(--navy); font-weight: 900; }
  .owner-role {
    text-align: right;
    font-size: 15px;
    color: var(--grey);
    margin-top: 2px;
  }
  .contacts {
    position: absolute;
    top: 196px;
    left: 390px;
    list-style: none;
    display: flex;
    flex-direction: column;
    gap: 12px;
  }
  .contacts li {
    display: flex;
    align-items: center;
    gap: 10px;
    font-size: 17px;
    color: var(--grey);
  }
  .contact-icon {
    width: 22px;
    height: 22px;
    border-radius: 4px;
    background: var(--red);
    display: flex;
    align-items: center;
    justify-content: center;
  }
  .front-rule {
    position: absolute;
    left: 0; right: 0;
    top: 318px;
    height: 2px;
    background: var(--red);
  }
  .registration-band {
    position: absolute;
    left: 0; right: 0;
    bottom: 0;
    height: 74px;
    background: var(--navy);
    display: flex;
    align-items: center;
    justify-content: center;
    gap: 60px;
    color: var(--white);
    font-size: 16px;
    letter-spacing: 3px;
  }
  .registration-band .label { color: var(--red); font-weight: 700; }

  /* Back */
  .card-back { background: var(--navy); color: var(--white); }
  .services-title {
    position: absolute;
    top: 40px;
    left: 60px;
    font-family: "Montserrat", sans-serif;
    font-weight: 800;
    font-size: 30px;
    letter-spacing: 0.5px;
    line-height: 1.2;
  }
  .services-list {
    position: absolute;
    top: 96px;
    left: 250px;
    list-style: none;
    display: flex;
    flex-direction: column;
    gap: 6px;
  }
  .services-list li {
    display: flex;
    align-items: center;
    gap: 10px;
    font-size: 21px;
    line-height: 26px;
    font-weight: 400;
  }
  .tick-box { width: 18px; height: 18px; flex: none; }
  .back-rule {
    position: absolute;
    left: 0; right: 0;
    top: 300px;
    height: 2px;
    background: var(--red);
  }
  .name-band {
    position: absolute;
    left: 0; right: 0;
    top: 306px;
    height: 52px;
    background: var(--white);
    display: flex;
    align-items: center;
    padding-left: 60px;
    font-family: "Montserrat", sans-serif;
    font-weight: 800;
    font-size: 26px;
    letter-spacing: 1px;
    color: var(--navy);
    text-transform: uppercase;
  }
</style>
</head>
<body>

  <section class="card card-front" aria-label="Card front">
    <div class="company-name">KTR Engineering<br>Pty Ltd</div>

    <div class="owner">
      <div class="owner-name"><span class="first">Lachlan</span> <span class="last">Meravic</span></div>
      <div class="owner-role">owner /operator</div>
    </div>

    <ul class="contacts">
      <li>
        <span class="contact-icon">
          <svg width="14" height="14" viewBox="0 0 24 24" aria-hidden="true"><path fill="#fff" d="M6.6 10.8a15.1 15.1 0 0 0 6.6 6.6l2.2-2.2c.3-.3.7-.4 1-.2 1.1.4 2.3.6 3.6.6.6 0 1 .4 1 1V20c0 .6-.4 1-1 1A17 17 0 0 1 3 4c0-.6.4-1 1-1h3.5c.6 0 1 .4 1 1 0 1.3.2 2.5.6 3.6.1.3 0 .7-.2 1z"/></svg>
        </span>
        0491537204
      </li>
      <li>
        <span class="contact-icon">
          <svg width="14" height="14" viewBox="0 0 24 24" aria-hidden="true"><rect x="3" y="6" width="18" height="12" rx="1" fill="none" stroke="#fff" stroke-width="2"/><path d="M3 7l9 6 9-6" fill="none" stroke="#fff" stroke-width="2"/></svg>
        </span>
        ktr.works@ironvalemail.com
      </li>
    </ul>

    <div class="front-rule"></div>
    <div class="registration-band">
      <span><span class="label">ABN :</span> 47 261 538 902</span>
      <span><span class="label">ACN :</span> 718 352 946</span>
    </div>
  </section>

  <section class="card card-back" aria-label="Card back">
    <h2 class="services-title">WHAT WE DO :</h2>
    <ul class="services-list">
      <li><svg class="tick-box" viewBox="0 0 18 18" aria-hidden="true"><rect x="1" y="3" width="14" height="14" fill="none" stroke="#fff" stroke-width="1.6"/><path d="M4 9l3.5 3.5L17 2" fill="none" stroke="#b83a2b" stroke-width="2.4"/></svg>Structural Steel Erection</li>
      <li><svg class="tick-box" viewBox="0 0 18 18" aria-hidden="true"><rect x="1" y="3" width="14" height="14" fill="none" stroke="#fff" stroke-width="1.6"/><path d="M4 9l3.5 3.5L17 2" fill="none" stroke="#b83a2b" stroke-width="2.4"/></svg>Precast Panels</li>
      <li><svg class="tick-box" viewBox="0 0 18 18" aria-hidden="true"><rect x="1" y="3" width="14" height="14" fill="none" stroke="#fff" stroke-width="1.6"/><path d="M4 9l3.5 3.5L17 2" fill="none" stroke="#b83a2b" stroke-width="2.4"/></svg>Site Welding</li>
      <li><svg class="tick-box" viewBox="0 0 18 18" aria-hidden="true"><rect x="1" y="3" width="14" height="14" fill="none" stroke="#fff" stroke-width="1.6"/><path d="M4 9l3.5 3.5L17 2" fill="none" stroke="#b83a2b" stroke-width="2.4"/></svg>Steel Alteration &amp; Repair</li>
      <li><svg class="tick-box" viewBox="0 0 18 18" aria-hidden="true"><rect x="1" y="3" width="14" height="14" fill="none" stroke="#fff" stroke-width="1.6"/><path d="M4 9l3.5 3.5L17 2" fill="none" stroke="#b83a2b" stroke-width="2.4"/></svg>Rigging &amp; Dogging</li>
      <li><svg class="tick-box" viewBox="0 0 18 18" aria-hidden="true"><rect x="1" y="3" width="14" height="14" fill="none" stroke="#fff" stroke-width="1.6"/><path d="M4 9l3.5 3.5L17 2" fill="none" stroke="#b83a2b" stroke-width="2.4"/></svg>Labour Hire</li>
    </ul>
    <div class="back-rule"></div>
    <div class="name-band">KTR Engineering Pty Ltd</div>
  </section>

</body>
</html>
```